Audio Visual & Broadcast Installing Company needs a Web Site Design

We need a website design for our company Halvern Crane Ltd. We are a small company that does Audio Visual and broadcast installations. We are looking to expand our business and need a professional web presence. All work completed by us is done to a very high standard and it’s this attention to detail that sets us apart from our competitors. Our projects include doing fibre optics at major sporting events; installing and commissioning bespoke control systems on super yachts and installing the latest systems in luxury homes.

We provide the following services:
System design
On-site installation
Rack building
Pre-fabricated cable looms
Fibre optic cabling

We would like a website that gives details of our services and provides contact information. Our customers are other businesses and our website needs to reflect this. The flyer attached will be used to promote the company and we would like the website to follow this theme. Please use the colours from our logo, as the colour scheme. We know that our colours are bright and we don’t want them to overwhelm the site. With our website we want to communicate that we are professional and provide a quality service.
NB UPDATE: please use stock images for any graphical elements.

The following 3 sites belong to some of our competitors. The first 2, we DON'T like because they don't project a professional feeling. The last one, 'lumatrexlinks', is better as it provides the required information in a clear, simple form.

http://www.qorvamedia.example/

http://www.pellisforthwiring.example/

http://www.lumatrexlinks.example/

We really like the following site, it feels professional and high end without too many flashy graphics. We want something that is fast to load but still shows the high end quality of our work.

http://oberlyncraft.example/

Pages/Sections

Home
On site installation
Rack building and cable looms
Fibre optics
Portfolio (this will be limited to start with but must be easy to expand and add new projects)
Updates

Target Market(s)

Businesses operating in the following areas:
Audio Vision, Broadcasting, Home Automation, Events

Industry/Entity Type

Broadcasting

Coding

Coded - Design and coding required

Number of Pages Required

4 page

Font styles to use
Other font styles liked:
• similar to attached flyer

Requirements
Must have
• The same theme as the 'flyer1' attachment.

```html
<!DOCTYPE html>
<html lang="en">
<head>
<meta charset="utf-8">
<title>Halvern Crane Ltd — Audio Visual &amp; Broadcast Installation</title>
<link rel="stylesheet" href="https://fonts.googleapis.com/css2?family=Montserrat:wght@400;500;600;700&family=Arimo:wght@400;700&display=swap">
<style>
:root{
  --red:#e2173d;
  --blue:#2987e4;
  --ink:#222222;
  --text:#555555;
  --muted:#777777;
  --light:#f4f4f4;
  --dark:#1c1a1a;
  --footer-bar:#3b3b3b;
  --white:#ffffff;
}
*{margin:0;padding:0;box-sizing:border-box}
html,body{width:1200px;height:2632px;overflow:hidden;background:var(--white)}
body{position:relative;font-family:"Arimo",Arial,sans-serif;color:var(--text)}
.abs{position:absolute}
.head{font-family:"Montserrat",Arial,sans-serif}

/* header */
.site-header{left:0;top:0;width:1200px;height:126px;background:var(--white);border-top:3px solid var(--red)}
.call-box{left:860px;top:0;width:340px;height:49px;background:var(--red);clip-path:polygon(0 0,100% 0,100% 100%,28px 100%);color:var(--white);display:flex;align-items:center;padding-left:34px;font-family:"Montserrat",sans-serif;font-size:17px;font-weight:500;gap:10px}
.call-box .sep{opacity:.8}
.brand{left:88px;top:34px;display:flex;align-items:center;gap:10px}
.brand .mark{width:30px;height:30px;background:var(--red)}
.brand .name{font-family:"Montserrat",sans-serif;font-weight:700;font-size:30px;color:var(--ink);letter-spacing:-.5px}
.main-nav{top:80px;left:0;width:1200px}
.main-nav a{position:absolute;transform:translateX(-50%);font-family:"Montserrat",sans-serif;font-size:13px;font-weight:500;color:var(--ink);text-decoration:none;white-space:nowrap}
.main-nav a.active{color:var(--red)}

/* hero */
.hero{left:0;top:126px;width:1200px;height:528px;background:linear-gradient(180deg,#8a7aa6 0%,#c59bb3 45%,#e7a9a6 70%,#6d5a66 100%)}
.hero-title{left:86px;top:264px;font-size:39px;font-weight:500;color:var(--red);letter-spacing:1px}
.hero-text{left:88px;top:326px;width:390px;font-size:13px;line-height:27px;color:#3a2f38}
.btn{display:flex;align-items:center;justify-content:center;background:var(--red);color:var(--white);font-family:"Montserrat",sans-serif;font-weight:600;border-radius:24px;text-decoration:none}
.hero-btn{left:88px;top:437px;width:147px;height:45px;font-size:15px}
.dots{left:98px;top:623px;display:flex;gap:7px}
.dots span{width:15px;height:15px;border:2px solid var(--white);border-radius:50%}
.dots span.on{background:var(--white)}

/* welcome */
.section-title{left:0;width:1200px;text-align:center;font-family:"Montserrat",sans-serif;font-weight:500;color:var(--red)}
.welcome-title{top:700px;font-size:23px}
.center-text{left:0;width:1200px;text-align:center;font-size:13px;line-height:26px;color:var(--text)}
.welcome-text{top:745px}
.feature{top:830px;width:495px;height:298px;overflow:hidden}
.feature.av{left:88px;background:linear-gradient(160deg,#2c2a2a,#5a5350 55%,#1f1d1c)}
.feature.bc{left:617px;background:linear-gradient(160deg,#c9c6bf,#9a958a 50%,#6b6a62)}
.feature-cap{left:0;bottom:0;width:100%;height:48px;background:rgba(20,20,20,.7);display:flex;align-items:center;justify-content:space-between;padding:0 15px;color:var(--white);font-family:"Montserrat",sans-serif;font-size:17px;font-weight:500}

/* services */
.services{left:0;top:1181px;width:1200px;height:428px;background:var(--light)}
.services-title{top:1220px;font-size:23px}
.services-text{top:1256px}
.service{top:1318px;width:230px;text-align:center;transform:translateX(-50%)}
.service .icon{width:122px;height:122px;border-radius:50%;margin:0 auto;display:flex;align-items:center;justify-content:center}
.service .icon.red{background:var(--red)}
.service .icon.blue{background:var(--blue)}
.service h3{font-family:"Montserrat",sans-serif;font-weight:500;font-size:17px;color:var(--ink);margin-top:12px}
.service p{font-size:13px;line-height:26px;margin-top:8px;color:var(--text)}
.svc-arrow{top:1430px}

/* rack band */
.rack-band{left:0;top:1609px;width:1200px;height:357px;background:radial-gradient(ellipse at 70% 70%,#4a3a30 0%,#221d1b 45%,#111 100%)}
.rack-title{left:0;top:1692px;width:1200px;text-align:center;font-size:28px;font-weight:500;color:var(--white)}
.rack-text{left:270px;top:1750px;width:660px;text-align:center;font-size:13px;line-height:26px;color:#eeeeee}
.rack-btn{left:475px;top:1852px;width:249px;height:50px;font-size:15px;font-weight:500}

/* testimonial */
.quote-mark{font-family:Georgia,serif;font-size:40px;color:#bbbbbb}
.quote-text{left:175px;top:2062px;width:545px;font-size:13px;line-height:23px;color:#333}
.quote-name{left:177px;top:2181px;font-family:"Arimo",sans-serif;font-weight:700;font-size:16px;color:var(--red)}
.quote-date{left:177px;top:2204px;font-size:13px;color:var(--text)}
.quote-photo{left:775px;top:2034px;width:194px;height:194px;border-radius:50%;border:4px solid #dddddd;background:linear-gradient(160deg,#d9cfc8,#b58e78 55%,#6e4d3c)}

/* footer */
.site-footer{left:0;top:2293px;width:1200px;height:275px;background:var(--white);border-top:1px solid #eeeeee}
.footer-brand{left:102px;top:2412px;display:flex;align-items:center;gap:10px}
.footer-brand .mark{width:36px;height:36px;background:var(--red)}
.footer-brand .name{font-family:"Montserrat",sans-serif;font-weight:700;font-size:32px;color:var(--ink);letter-spacing:-.5px}
.footer-col h4{font-family:"Montserrat",sans-serif;font-weight:500;font-size:17px;color:var(--ink)}
.contact-list{list-style:none;margin-top:26px}
.contact-list li{display:flex;gap:12px;font-size:13px;line-height:16px;color:var(--text);margin-bottom:13px}
.contact-list svg{flex:none;margin-top:1px}
.contact-list a{color:var(--text)}
.footer-col p{font-size:13px;line-height:21px;margin-top:24px}
.email-field{margin-top:16px;width:212px;height:34px;border:1px solid #cccccc;font-size:13px;padding:0 12px;display:flex;align-items:center;color:#444}
.subscribe{margin-top:8px;width:81px;height:29px;background:var(--red);color:var(--white);font-size:12px;display:flex;align-items:center;justify-content:center}
.social{display:flex;gap:7px;margin-top:18px}
.social span{width:36px;height:36px;border:2px solid #999999;border-radius:50%}

.copyright{left:0;top:2568px;width:1200px;height:64px;background:var(--footer-bar);color:var(--white);font-size:13px;display:flex;align-items:center;justify-content:center}
</style>
</head>
<body>

<header class="abs site-header">
  <div class="abs call-box"><svg width="14" height="14" viewBox="0 0 24 24"><path fill="#fff" d="M6.6 10.8a15 15 0 0 0 6.6 6.6l2.2-2.2c.3-.3.7-.4 1-.2 1.1.4 2.3.6 3.6.6.6 0 1 .4 1 1V20c0 .6-.4 1-1 1A17 17 0 0 1 3 4c0-.6.4-1 1-1h3.5c.6 0 1 .4 1 1 0 1.3.2 2.5.6 3.6.1.3 0 .7-.2 1z"/></svg><span class="sep">|</span><span>CALL US : 0161 555-0192</span></div>
  <div class="abs brand"><span class="mark"></span><span class="name">Halvern Crane</span></div>
  <nav class="abs main-nav">
    <a class="active" style="left:344px">HOME</a>
    <a style="left:468px">ON SITE INSTALLATION</a>
    <a style="left:674px">RACK BUILDING &amp; CABLE LOOMS</a>
    <a style="left:851px">FIBRE OPTICS</a>
    <a style="left:963px">PORTFOLIO</a>
    <a style="left:1074px">CONTACT US</a>
  </nav>
</header>

<section class="abs hero" role="img" aria-label="Satellite dish silhouetted against a pink sunset sky"></section>
<h1 class="abs head hero-title">HALVERN-CRANE</h1>
<p class="abs hero-text">Halvern Crane provide cabling services for the Broadcast and Audio Visual industries. We specialise in the neat and clean installation which has come to be expected on high end systems.</p>
<a class="abs btn hero-btn">READ MORE</a>
<div class="abs dots"><span></span><span class="on"></span><span></span><span></span></div>

<h2 class="abs section-title welcome-title">WELCOME TO HALVERN-CRANE</h2>
<p class="abs center-text welcome-text">Halvern Crane provide cabling services for the Broadcast and Audio Visual industries. We specialise in the neat and clean<br>installation which has come to be expected on high end systems.</p>

<div class="abs feature av" role="img" aria-label="Studio mixing desk with monitors">
  <div class="abs feature-cap"><span>AUDIO VISUAL</span><svg width="16" height="16" viewBox="0 0 16 16"><circle cx="8" cy="8" r="6.5" fill="none" stroke="#fff" stroke-width="1.6"/><path d="M7 5l3 3-3 3" fill="none" stroke="#fff" stroke-width="1.6"/></svg></div>
</div>
<div class="abs feature bc" role="img" aria-label="Engineer installing a satellite dish at a house">
  <div class="abs feature-cap"><span>BROADCAST INSTALLATIONS</span><svg width="16" height="16" viewBox="0 0 16 16"><circle cx="8" cy="8" r="6.5" fill="none" stroke="#fff" stroke-width="1.6"/><path d="M7 5l3 3-3 3" fill="none" stroke="#fff" stroke-width="1.6"/></svg></div>
</div>

<section class="abs services"></section>
<h2 class="abs section-title services-title">OUR SERVICES</h2>
<p class="abs center-text services-text">Halvern Crane provide cabling services for the Broadcast and Audio Visual specialise in the neat industries.</p>

<svg class="abs svc-arrow" style="left:34px" width="22" height="100" viewBox="0 0 22 100"><path d="M20 2L2 50l18 48" fill="none" stroke="#cccccc" stroke-width="2"/></svg>
<svg class="abs svc-arrow" style="left:1144px" width="22" height="100" viewBox="0 0 22 100"><path d="M2 2l18 48L2 98" fill="none" stroke="#cccccc" stroke-width="2"/></svg>

<div class="abs service" style="left:216px">
  <div class="icon red"><svg width="62" height="62" viewBox="0 0 62 62" fill="none" stroke="#fff" stroke-width="3"><rect x="6" y="10" width="46" height="32" rx="2"/><path d="M22 52h18M31 42v10"/><path d="M20 34l22-20 4 4-22 20-6 2z" fill="#fff"/></svg></div>
  <h3>SYSTEM DESIGN</h3>
  <p>Halvern Crane provide cabling services for the Broadcast and Audio Visual in the neat industries.</p>
</div>
<div class="abs service" style="left:474px">
  <div class="icon blue"><svg width="62" height="62" viewBox="0 0 62 62" fill="none" stroke="#fff" stroke-width="5" stroke-linecap="round"><path d="M14 48L40 22"/><circle cx="45" cy="17" r="7" stroke-width="4"/><path d="M14 14l34 34"/><path d="M10 10l6 6" stroke-width="7"/></svg></div>
  <h3>ON-SITE INSTALLATION</h3>
  <p>Halvern Crane provide cabling services for the Broadcast and Audio Visual in the neat industries.</p>
</div>
<div class="abs service" style="left:730px">
  <div class="icon red"><svg width="62" height="62" viewBox="0 0 62 62" fill="none" stroke="#fff" stroke-width="3"><rect x="18" y="8" width="26" height="46"/><path d="M12 54h38"/><g fill="#fff" stroke="none"><rect x="23" y="14" width="5" height="5"/><rect x="34" y="14" width="5" height="5"/><rect x="23" y="24" width="5" height="5"/><rect x="34" y="24" width="5" height="5"/><rect x="23" y="34" width="5" height="5"/><rect x="34" y="34" width="5" height="5"/><rect x="28" y="44" width="6" height="10"/></g></svg></div>
  <h3>RACK BUILDING</h3>
  <p>Halvern Crane provide cabling services for the Broadcast and Audio Visual in the neat industries.</p>
</div>
<div class="abs service" style="left:988px">
  <div class="icon blue"><svg width="62" height="62" viewBox="0 0 62 62" fill="none" stroke="#fff" stroke-width="3" stroke-linecap="round"><path d="M8 54l16-16M24 38l6-22M24 38l14-8M24 38l22 4M30 16l4-8M38 30l12-10M46 42l8 6"/><g fill="#fff"><circle cx="34" cy="8" r="3"/><circle cx="50" cy="20" r="3"/><circle cx="54" cy="48" r="3"/><circle cx="30" cy="16" r="2"/></g></svg></div>
  <h3>FIBRE OPTIC CABLING</h3>
  <p>Halvern Crane provide cabling services for the Broadcast and Audio Visual in the neat industries.</p>
</div>

<section class="abs rack-band" role="img" aria-label="Blurred mixing console in a dark control room"></section>
<h2 class="abs head rack-title">RACK BUILDING &amp; CABLE LOOMS</h2>
<p class="abs rack-text">Halvern Crane provide cabling services for the Broadcast and Audio Visual industries. We specialise in the neat and clean installation which has come to be expected on high end systems. This helps us to achieve a robust and easily maintained services for the Broadcast and Audio installation that you can depend on.</p>
<a class="abs btn rack-btn">CLICK HERE FOR MORE INFO</a>

<span class="abs quote-mark" style="left:156px;top:2034px">“</span>
<p class="abs quote-text">Sed ut perspiciatis unde omnis iste natus error sit voluptatem accusantium doloremque laudantium, totam rem aperiam, eaque ipsa quae ab illo inventore veritatis et quasi architecto beatae vitae dicta sunt explicabo. Nemo enim ipsam voluptatem quia voluptas sit aspernatur aut odit aut fugit, sed quia consequuntur magni dolores eos qui ratione voluptatem sequi nesciunt.</p>
<span class="abs quote-mark" style="left:558px;top:2140px">”</span>
<p class="abs quote-name">DARA COLWELL</p>
<p class="abs quote-date">Posted On 07 Dec 2017</p>
<div class="abs quote-photo" role="img" aria-label="Portrait of the client giving the testimonial"></div>

<footer class="abs site-footer"></footer>
<div class="abs footer-brand"><span class="mark"></span><span class="name">Halvern Crane</span></div>

<div class="abs footer-col" style="left:395px;top:2350px;width:220px">
  <h4>CONTACT US</h4>
  <ul class="contact-list">
    <li><svg width="14" height="14" viewBox="0 0 24 24"><path fill="#666" d="M6.6 10.8a15 15 0 0 0 6.6 6.6l2.2-2.2c.3-.3.7-.4 1-.2 1.1.4 2.3.6 3.6.6.6 0 1 .4 1 1V20c0 .6-.4 1-1 1A17 17 0 0 1 3 4c0-.6.4-1 1-1h3.5c.6 0 1 .4 1 1 0 1.3.2 2.5.6 3.6.1.3 0 .7-.2 1z"/></svg>0161 555-0192 (Phone)</li>
    <li><svg width="14" height="14" viewBox="0 0 14 14"><rect x="3" y="1" width="8" height="4" fill="#666"/><rect x="1" y="5" width="12" height="6" fill="#666"/><rect x="3" y="9" width="8" height="4" fill="#fff" stroke="#666"/></svg>0161 555-0193 (Fax)</li>
    <li><svg width="14" height="14" viewBox="0 0 14 14"><rect x="1" y="3" width="12" height="8" fill="#666"/><path d="M1 3l6 5 6-5" fill="none" stroke="#fff"/></svg><a>info@halverncrane.example</a></li>
    <li><svg width="14" height="14" viewBox="0 0 14 14"><path d="M7 1a4 4 0 0 1 4 4c0 3-4 8-4 8S3 8 3 5a4 4 0 0 1 4-4z" fill="#666"/><circle cx="7" cy="5" r="1.5" fill="#fff"/></svg>123 Street Landmark,Country<br>123456</li>
  </ul>
</div>

<div class="abs footer-col" style="left:640px;top:2350px;width:220px">
  <h4>NEWSLETTER</h4>
  <p>Register Your email address to get information ablout us</p>
  <div class="email-field">Email Address</div>
  <div class="subscribe">SUBSCRIBE</div>
</div>

<div class="abs footer-col" style="left:893px;top:2352px;width:220px">
  <h4>FOLLOW US</h4>
  <p style="margin-top:22px;width:200px">Lorem ipsum dolor sit amet, conse ctetur adipiscing elit. Nulla in purus nibh. Donec ornare</p>
  <div class="social"><span></span><span></span><span></span><span></span><span></span></div>
</div>

<div class="abs copyright">© Copyright 2017 Halvern Crane.All Rights Reserved</div>

</body>
</html>
```